Business cards for Paperleaf Sprites

Please note that the color of the logo has been changed from green to teal blue. Sorry for the changing!

Anything will go but want to have some funky side.

I would like the front of the business card is the logo and business information and the back side is the Adult Coloring, so that would attract the customer to do the coloring on the other side. Have more interactive side. (pictures for references only can see it below). Fairies on the back of the card for coloring and whatever you want to adds on to color, like flowers, nature etc......

Scrapbooking is not just paper, it also involves watercolor, mixed media, art, all the fun stuff.

Another keypoint I would like to stress on is the back of the business card should be Adult Coloring and make sure you are not google and use the search engine to copy and paste because of the copyright issue.

As a designer, I am sure you all can create beautiful artwork.

Please submit your creativities!

Want the business card is out of the ordinary and customers would like to keep that as a keepsake rather than treat like a regular business card and trash it. Fonts cannot be too small, consider some of the customers have to wear bi-focal eyeglasses.

Thanks a lot!

Target Market(s)

Scrapbooking, Card making, papercraft, stampin‘ , gifts items , etc.

Industry/Entity Type

Retail

Contact Information for Business Card

Color Scheme, please match with the Logo. Watercolor effect is nice!
Thanks!

Font styles to use
Serif

Requirements
Must have
• I would like Elegant and playful.
• Thanks!
Nice to have
• Watercolor effect or check out the Adult Coloring Book, I am thinking we can use a double-sided business card, one side for the information and the other side for people can do the coloring. I have attached 2 pictures for reference.
Should not have
• No black color on the background please!

```html
<!DOCTYPE html>
<html lang="en">
<head>
<meta charset="utf-8">
<title>Paperleaf Sprites – Business Cards</title>
<link rel="stylesheet" href="https://fonts.googleapis.com/css2?family=Lora:wght@400;600;700&display=swap">
<style>
  :root {
    --bg: #ece5dc;
    --card: #f8f8f6;
    --teal: #1f8388;
    --teal-soft: #cfe7e6;
    --petal-soft: #f3dcd8;
    --berry-red: #a13a2c;
    --ink-grey: #555555;
    --rule: #d8d8d4;
  }
  * { box-sizing: border-box; margin: 0; padding: 0; }
  html, body {
    width: 1200px; height: 794px; overflow: hidden;
    background: var(--bg);
    font-family: "Lora", Georgia, serif;
  }
  .canvas {
    width: 1200px; height: 794px;
    display: flex; flex-direction: column; align-items: center; justify-content: center;
    gap: 40px;
  }
  .card {
    width: 640px; height: 360px;
    background: var(--card);
    box-shadow: 0 2px 6px rgba(0,0,0,0.12);
    position: relative;
  }

  /* Front: colouring side with the brand name */
  .card--front { display: flex; align-items: center; justify-content: center; }
  .colouring-art {
    position: absolute; inset: 18px;
    background:
      radial-gradient(circle at 22% 30%, var(--petal-soft) 0, transparent 38%),
      radial-gradient(circle at 78% 70%, var(--teal-soft) 0, transparent 42%),
      radial-gradient(circle at 70% 22%, #e6efd9 0, transparent 32%),
      #fbfbf9;
    border: 1px solid var(--rule);
  }
  .brand-plate {
    position: relative;
    background: var(--card);
    padding: 18px 30px;
    border: 1px solid var(--rule);
  }

  .brand {
    display: flex; align-items: center; gap: 12px;
    color: var(--teal);
    font-weight: 700;
    letter-spacing: 0.5px;
    white-space: nowrap;
  }
  .brand__dot {
    width: 18px; height: 18px; border-radius: 50%;
    background: var(--teal);
    flex: none;
  }
  .card--front .brand { font-size: 40px; }
  .card--back .brand { font-size: 27px; }
  .card--back .brand__dot { width: 13px; height: 13px; }

  /* Back: brand and contact details */
  .card--back { display: flex; }
  .card__brand-side {
    width: 55%;
    display: flex; align-items: center; justify-content: center;
  }
  .card__divider { width: 1px; background: var(--rule); margin: 42px 0 24px; }
  .contact { flex: 1; padding: 54px 0 0 28px; color: var(--ink-grey); }
  .contact__name { color: var(--teal); font-weight: 600; font-size: 21px; line-height: 1.1; }
  .contact__role { color: var(--berry-red); font-size: 14px; margin-bottom: 16px; }
  .contact__address { font-size: 14px; line-height: 1.45; margin-bottom: 10px; }
  .contact__list { list-style: none; font-size: 14px; line-height: 1.75; }
  .contact__list li { display: flex; align-items: center; gap: 9px; white-space: nowrap; }
  .contact__icon { width: 14px; height: 14px; flex: none; }
</style>
</head>
<body>
<main class="canvas">
  <section class="card card--front" aria-label="Card front, colouring side">
    <div class="colouring-art" role="img" aria-label="Line-art fairies among flowers and leaves for colouring in, with soft watercolour washes"></div>
    <div class="brand-plate">
      <div class="brand"><span class="brand__dot"></span><span>Paperleaf Sprites</span></div>
    </div>
  </section>

  <section class="card card--back" aria-label="Card back">
    <div class="card__brand-side">
      <div class="brand"><span class="brand__dot"></span><span>Paperleaf Sprites</span></div>
    </div>
    <div class="card__divider"></div>
    <div class="contact">
      <p class="contact__name">CLARA HOLLIS</p>
      <p class="contact__role">CEO/FOUNDER</p>
      <p class="contact__address">2140 Willow Bend Road<br>Juneau, Alaska 99801</p>
      <ul class="contact__list">
        <li>
          <svg class="contact__icon" viewBox="0 0 16 16" aria-hidden="true"><path fill="var(--teal)" d="M3.6 1.5l2.3 2.6-1.3 1.6c.9 2 2.4 3.6 4.5 4.6l1.6-1.3 2.6 2.3-1 2.3C7.1 13.4 2.6 8.9 1.4 3.5z"/></svg>
          555 204 7719
        </li>
        <li>
          <svg class="contact__icon" viewBox="0 0 16 16" aria-hidden="true"><rect x="1" y="3.5" width="14" height="9.5" fill="var(--teal)"/><path d="M1.5 4l6.5 5 6.5-5" fill="none" stroke="#fff" stroke-width="1.2"/></svg>
          hello@paperleafsprites.com
        </li>
        <li>
          <svg class="contact__icon" viewBox="0 0 16 16" aria-hidden="true"><circle cx="8" cy="8" r="7" fill="var(--teal)"/><path d="M1 8h14M8 1c-3 3.5-3 10.5 0 14M8 1c3 3.5 3 10.5 0 14" fill="none" stroke="#fff" stroke-width="1"/></svg>
          www.paperleafsprites.com
        </li>
      </ul>
    </div>
  </section>
</main>
</body>
</html>
```